Business Card Design

I am nail technician working from home in Fernwick Rise, Perth and I require new business cards. I only work with Gel medium for nail extensions using tips or I can also do sculpture nails. I specialise in hand painted nail art using water based acrylic paint and nail polish. As the name suggest I love all things "Shimmer" so I would love something that reflects this while also being professional. I'm also on Chatterly and would the Chatterly logo.

Contact Information for Business Card

Shimmer Bay nail designs,Rosanne ,0417859263, ShimmerBaynaildesigns@quellmail.com, nail technician specialising in hand painted nail art, only using a Gel medium

```html
<!DOCTYPE html>
<html lang="en">
<head>
<meta charset="utf-8">
<title>Shimmer Bay Nail Designs – Business Card</title>
<link rel="stylesheet" href="https://fonts.googleapis.com/css2?family=Exo+2:wght@400;500;600&display=swap">
<style>
  :root {
    --backdrop: #c9cbcf;
    --card: #3e4450;
    --card-deep: #353a45;
    --red: #e3101f;
    --red-dark: #b80c18;
    --tile-grey: #6a707b;
    --tile-grey-dark: #575c66;
    --ink-light: #dde0e5;
    --white: #ffffff;
    --pearl: #f3f1f4;
  }
  * { box-sizing: border-box; margin: 0; padding: 0; }
  html, body {
    width: 1200px; height: 861px; overflow: hidden;
    background: var(--backdrop);
    font-family: "Exo 2", sans-serif;
  }
  .business-card {
    position: absolute; left: 100px; top: 145px;
    width: 1000px; height: 571px;
    background: linear-gradient(160deg, var(--card) 0%, var(--card-deep) 100%);
    overflow: hidden;
    box-shadow: 0 14px 30px rgba(0,0,0,.25);
  }
  .name-band {
    position: absolute; left: 0; top: 38px;
    width: 790px; height: 56px;
    background: linear-gradient(100deg, var(--red) 0%, #f0323f 45%, var(--red) 60%, var(--red-dark) 100%);
    display: flex; align-items: center; gap: 14px;
    padding-left: 40px;
    color: var(--white);
  }
  .name-band .person { font-size: 26px; font-weight: 500; letter-spacing: 1px; text-transform: uppercase; white-space: nowrap; }
  .name-band .role { font-size: 17px; font-weight: 400; white-space: nowrap; }
  .channel-row {
    position: absolute; left: 40px; top: 130px;
    display: flex; gap: 98px;
  }
  .channel { width: 138px; }
  .tile {
    width: 118px; height: 118px;
    border: 3px solid rgba(255,255,255,.85);
    border-radius: 8px;
    display: flex; flex-direction: column; align-items: center; justify-content: center; gap: 10px;
    color: var(--white); font-size: 16px; font-weight: 500;
  }
  .tile--red { background: linear-gradient(180deg, var(--red) 0%, var(--red-dark) 100%); }
  .tile--grey { background: linear-gradient(180deg, var(--tile-grey) 0%, var(--tile-grey-dark) 100%); }
  .tile .mark { width: 40px; height: 40px; }
  .tile .plain-square { width: 34px; height: 34px; border: 3px solid var(--white); border-radius: 4px; }
  .channel-detail {
    margin-top: 12px; width: 200px;
    color: var(--ink-light); font-size: 16px; line-height: 1.3;
  }
  .contact-line {
    position: absolute; left: 40px; top: 350px;
    display: flex; gap: 34px; align-items: center;
    color: var(--ink-light); font-size: 17px; letter-spacing: .3px;
    white-space: nowrap;
  }
  .contact-line .item { display: flex; align-items: center; gap: 8px; }
  .contact-line svg { width: 18px; height: 18px; flex: none; }
  .brand-band {
    position: absolute; left: 0; top: 400px;
    width: 100%; height: 171px;
    background: linear-gradient(115deg, var(--white) 0%, var(--pearl) 35%, var(--white) 50%, var(--pearl) 70%, var(--white) 100%);
  }
  .brand {
    position: absolute; left: 280px; top: 34px;
    color: var(--red); font-weight: 500;
  }
  .brand .brand-name { display: block; font-size: 64px; line-height: 1; letter-spacing: 1px; }
  .brand .brand-sub { display: block; font-size: 28px; margin-top: 4px; margin-left: 170px; }
</style>
</head>
<body>
  <main class="business-card">
    <header class="name-band">
      <span class="person">Rosanne Vale</span>
      <span class="role">Nail Technician · Hand Painted Nail Art · Gel</span>
    </header>

    <section class="channel-row">
      <div class="channel">
        <div class="tile tile--red">
          <svg class="mark" viewBox="0 0 40 40" aria-hidden="true">
            <path d="M4 20 L20 6 L36 20" fill="none" stroke="#fff" stroke-width="4" stroke-linejoin="round"/>
            <rect x="10" y="19" width="20" height="16" fill="#fff"/>
            <rect x="17" y="25" width="6" height="10" fill="#e3101f"/>
          </svg>
          <span>Address</span>
        </div>
        <p class="channel-detail">Fernwick Rise<br>Perth WA</p>
      </div>
      <div class="channel">
        <div class="tile tile--grey">
          <span class="plain-square"></span>
          <span>Chatterly</span>
        </div>
        <p class="channel-detail">chatterly.com<br>/shimmerbay</p>
      </div>
      <div class="channel">
        <div class="tile tile--grey">
          <span class="plain-square"></span>
          <span>Chirpline</span>
        </div>
        <p class="channel-detail">@shimmerbay</p>
      </div>
      <div class="channel">
        <div class="tile tile--red">
          <span class="plain-square"></span>
          <span>Linkwell</span>
        </div>
        <p class="channel-detail">Rosanne Vale</p>
      </div>
    </section>

    <section class="contact-line">
      <span class="item">
        <svg viewBox="0 0 18 18" aria-hidden="true"><path d="M4 2 L7 2 L8 6 L6 7.5 C7 10 8.5 11.5 11 12.5 L12.5 10.5 L16 11.5 L16 14.5 C16 15.5 15 16 14 16 C8 15.5 2.5 10 2 4 C2 3 3 2 4 2 Z" fill="#dde0e5"/></svg>
        0417 859 263
      </span>
      <span class="item">
        <svg viewBox="0 0 18 18" aria-hidden="true"><rect x="1.5" y="4" width="15" height="10" fill="#dde0e5"/><path d="M1.5 4 L9 10 L16.5 4" fill="none" stroke="#3e4450" stroke-width="1.5"/></svg>
        ShimmerBaynaildesigns@quellmail.com
      </span>
      <span class="item">
        <svg viewBox="0 0 18 18" aria-hidden="true"><circle cx="9" cy="9" r="7" fill="none" stroke="#dde0e5" stroke-width="1.6"/><ellipse cx="9" cy="9" rx="3" ry="7" fill="none" stroke="#dde0e5" stroke-width="1.4"/><line x1="2" y1="9" x2="16" y2="9" stroke="#dde0e5" stroke-width="1.4"/></svg>
        www.shimmerbaynails.com
      </span>
    </section>

    <footer class="brand-band">
      <div class="brand">
        <span class="brand-name">Shimmer Bay</span>
        <span class="brand-sub">Nail Designs</span>
      </div>
    </footer>
  </main>
</body>
</html>
```